Business Card Design for a Handbags business

We are modernising our handbags website (see attached file for new front page) and are in need of a modern business card and a related design we can use on a small marquee at the markets, on letterhead, emails etc.

As the leather handbags we mostly import are from Italy, we want a smart modern European feel to the design. We are currently thinking about changing the name of the business from Meadowlark Handbags (see www.meadowlarkhandbags.com.au) to Vantera Handbags. Also open to other suggestions you may have that communicates the European influence and quality.

Target Market(s)

25-65 year old women (and some men)

Industry/Entity Type

Business

Contact Information for Business Card

Single or double sided - whichever creates more of an impact

Font styles to use
Serif
Sans Serif

Requirements
Must have
• Clean crisp look, slightly Italian or European look and feel to reflect where the handbags are imported from
Nice to have
• open to ideas

```html
<!DOCTYPE html>
<html lang="en">
<head>
<meta charset="utf-8">
<title>Meadowlark Handbags &amp; Accessories – Business Card</title>
<link rel="stylesheet" href="https://fonts.googleapis.com/css2?family=Great+Vibes&family=Fondamento&display=swap">
<style>
  :root {
    --backdrop: #e9ebea;
    --card: #ffffff;
    --ink: #2c2b2a;
    --band: #2d2c2b;
    --paper-line: #ffffff;
  }
  * { box-sizing: border-box; margin: 0; padding: 0; }
  html, body {
    width: 1200px;
    height: 934px;
    overflow: hidden;
    background: var(--backdrop);
  }
  .canvas {
    position: relative;
    width: 1200px;
    height: 934px;
  }
  .card {
    position: absolute;
    left: 153px;
    top: 200px;
    width: 906px;
    height: 557px;
    background: var(--card);
    overflow: hidden;
  }
  .business-name {
    position: absolute;
    left: 0;
    right: 0;
    top: 124px;
    text-align: center;
    font-family: "Great Vibes", cursive;
    font-weight: 400;
    font-size: 56px;
    word-spacing: 4px;
    line-height: 1;
    white-space: nowrap;
    color: var(--ink);
  }
  .owner-name {
    position: absolute;
    left: 0;
    right: 0;
    top: 252px;
    text-align: center;
    font-family: "Fondamento", serif;
    font-size: 30px;
    letter-spacing: 1.5px;
    word-spacing: 4px;
    color: var(--ink);
  }
  .footer-band {
    position: absolute;
    left: 0;
    right: 0;
    top: 377px;
    bottom: 0;
    background: var(--band);
  }
  .band-rule {
    position: absolute;
    left: 0;
    right: 0;
    top: 389px;
    height: 6px;
    background: var(--paper-line);
  }
  .contact {
    position: absolute;
    top: 492px;
    display: flex;
    align-items: center;
    gap: 14px;
    font-family: "Fondamento", serif;
    font-size: 31px;
    color: var(--paper-line);
    letter-spacing: 1px;
    word-spacing: 4px;
    white-space: nowrap;
  }
  .contact--phone { left: 129px; }
  .contact--location { left: 494px; gap: 6px; }
  .contact svg { display: block; fill: var(--paper-line); }
</style>
</head>
<body>
<main class="canvas">
  <section class="card">
    <h1 class="business-name">Meadowlark Handbags &amp; Accessories</h1>
    <p class="owner-name">Clara Bennett</p>

    <div class="footer-band"></div>
    <div class="band-rule"></div>

    <p class="contact contact--phone">
      <svg width="16" height="26" viewBox="0 0 16 26" aria-hidden="true">
        <path d="M3 0h10a3 3 0 0 1 3 3v20a3 3 0 0 1-3 3H3a3 3 0 0 1-3-3V3a3 3 0 0 1 3-3zm-0.5 4v15h11V4zm5.5 17.5a1.3 1.3 0 1 0 0 .01z"/>
      </svg>
      <span>0412 555 019</span>
    </p>

    <p class="contact contact--location">
      <svg width="20" height="30" viewBox="0 0 20 30" aria-hidden="true">
        <path d="M10 0a10 10 0 0 1 10 10c0 7-10 20-10 20S0 17 0 10A10 10 0 0 1 10 0zm0 5.5a4.5 4.5 0 1 0 0 9 4.5 4.5 0 0 0 0-9z"/>
      </svg>
      <span>Wrenfield, Brisbane</span>
    </p>
  </section>
</main>
</body>
</html>
```